Social responsible Renewable Energy company

We at voltaQ are an independent power producer company founded in 2021 that handles large scale deployment of Renewable Energy and carbon neutral Energy as a service model. We offer turnkey solutions using solar panel systems and this could be incorporated in our business cards. You can also find our logo in the documents provided. Another key issue is that the business cards will be printed on recicled paper, not sure if this is a limitation in deciding the design. The recycled sign should also be added on the business card and stating that the paper used was recycled. Our website is www.myvoltaq.example. It should also be very professional, not too dreamy but still needs to capture your imagination. We are really excited to get your ideas !

Target Market(s)

Renewable Energy market

Contact Information for Business Card

The business card will be printed on recycled paper. Name of the company is voltaQ. Website is www.myvoltaq.example

Requirements
Nice to have
• Our motto: Powered by renewable, driven by people.

```html
<!DOCTYPE html>
<html lang="en">
<head>
<meta charset="utf-8">
<title>voltaQ business card</title>
<link href="https://fonts.googleapis.com/css2?family=Open+Sans:wght@400;700&display=swap" rel="stylesheet">
<style>
  :root {
    --backdrop: #e3cdbb;
    --kraft: #b8a38c;
    --kraft-edge: #a8927a;
    --ink: #2a2420;
    --ink-soft: #3d3530;
  }
  * { margin: 0; padding: 0; box-sizing: border-box; }
  html, body {
    width: 1200px; height: 880px; overflow: hidden;
    background: var(--backdrop);
    font-family: "Open Sans", Arial, sans-serif;
    color: var(--ink);
  }
  .sheet {
    width: 1200px; height: 880px;
    display: flex; flex-direction: column;
    align-items: center; justify-content: center; gap: 44px;
  }
  .card {
    position: relative;
    width: 588px; height: 350px;
    background: var(--kraft);
    border-radius: 14px;
    box-shadow: inset 0 0 0 3px var(--kraft-edge);
  }
  /* front side */
  .brand-name {
    position: absolute; left: 40px; top: 150px;
    font-size: 50px; font-weight: 700; letter-spacing: 0.5px;
    color: var(--ink);
  }
  .divider {
    position: absolute; left: 262px; top: 92px;
    width: 2px; height: 172px; background: var(--ink-soft);
  }
  .contact {
    position: absolute; left: 282px; top: 86px;
    font-size: 13.5px; line-height: 20px; color: var(--ink-soft);
  }
  .contact-name {
    font-size: 19px; font-weight: 700; line-height: 24px;
    letter-spacing: 0.6px; color: var(--ink);
  }
  .contact-title { margin-bottom: 18px; }
  .contact-address { margin-bottom: 16px; }
  .contact-line { display: flex; align-items: center; gap: 6px; line-height: 22px; }
  .contact-line svg { width: 12px; height: 12px; fill: var(--ink-soft); flex: none; }
  .paper-badges {
    position: absolute; right: 34px; bottom: 26px;
    display: flex; align-items: flex-start; gap: 10px;
  }
  .badge-recycled { width: 24px; height: 24px; border-radius: 50%; background: var(--ink-soft); }
  .badge-certificate { width: 48px; height: 56px; border-radius: 6px; background: var(--ink-soft); }
  /* back side */
  .back-brand {
    position: absolute; left: 0; right: 0; top: 120px;
    text-align: center; font-size: 50px; font-weight: 700; color: var(--ink);
  }
  .motto {
    position: absolute; left: 0; right: 0; bottom: 40px;
    text-align: center; font-size: 12px; color: var(--ink-soft);
  }
</style>
</head>
<body>
<main class="sheet">
  <section class="card card-front" aria-label="Card front">
    <div class="brand-name">voltaQ</div>
    <div class="divider"></div>
    <div class="contact">
      <div class="contact-name">ELLIOT MARSH</div>
      <div class="contact-title">President</div>
      <div class="contact-address">1480 Harbor Crest Way<br>Lumen Bay CA 90210</div>
      <div class="contact-line">
        <svg viewBox="0 0 24 24" aria-hidden="true"><path d="M6.6 10.8c1.4 2.8 3.8 5.1 6.6 6.6l2.2-2.2c.3-.3.7-.4 1-.2 1.1.4 2.3.6 3.6.6.6 0 1 .4 1 1V20c0 .6-.4 1-1 1C10.6 21 3 13.4 3 4c0-.6.4-1 1-1h3.5c.6 0 1 .4 1 1 0 1.3.2 2.5.6 3.6.1.3 0 .7-.2 1l-2.3 2.2z"/></svg>
        <span>555-014-2387</span>
      </div>
      <div class="contact-line">
        <svg viewBox="0 0 24 24" aria-hidden="true"><path d="M2 5h20v14H2z M4 7v.5l8 5 8-5V7l-8 5z" fill-rule="evenodd"/></svg>
        <span>emarsh@myvoltaq.example</span>
      </div>
      <div class="contact-line">
        <svg viewBox="0 0 24 24" aria-hidden="true"><circle cx="12" cy="12" r="10"/></svg>
        <span>www.myvoltaq.example</span>
      </div>
    </div>
    <div class="paper-badges">
      <div class="badge-recycled" role="img" aria-label="Recycled paper mark"></div>
      <div class="badge-certificate" role="img" aria-label="Forest certification mark"></div>
    </div>
  </section>

  <section class="card card-back" aria-label="Card back">
    <div class="back-brand">voltaQ</div>
    <p class="motto">Powered by renewable, driven by people.</p>
  </section>
</main>
</body>
</html>
```